new dating app design - young, fresh, clean

Project Brief

Vimzy is the world's first dating app that actually arranges dates. The process consists of 3 easy steps:

1. use our calendar to tell us when you'd like a date
2. browse singles nearby and select who you'd like to meet
3. when your date is 1 hour away, the app will find you a nice venue in the neighborhood and send one of your matches there to meet you. All you need to do is show up and have a good time.

This design assignment consists of creating a fun, fresh & user-friendly design for the wireframes created by our UX designer. Included are 2 screens:

1. the 'calendar' screen

2. the 'matches' screen

Also included is our style guide for your reference. Feel free to use as much or as little from this guide as you please. It would be nice if we could remain somewhat consistent with our previous design (which was purely based on this style guide) but we also want you to be creative and show off your skills so by no means should you feel obliged to conform to it.

Things to consider

1. 'calendar'

this is where you tell the app when you're free for a date. You can select as many time slots as you want. The info bars at the top and the bottom are 'sticky' (will stay in place no matter where in the screen you scroll to).

Everything about this page needs to be designed: not just in terms of spacing, font and coloring of the calendar itself but also the sticky bars at the bottom and top, and the interactions (when you select a time slot, what happens visually? How will it show that this slot was selected?).

TIP: please ignore the black vs white time slot distribution you see in the image. This was meant to signify where daytime becomes nighttime and vice versa, but we're not doing that anymore. So the only difference between blocks will be the difference between a selected and an unselected block. Make sure that difference is clearly visible in your design.

2. 'matches'

this is where you tell the app whom you'd like to meet with. You can select as many people as you want by clicking their 'heart' icon. You can scroll down to see more people and again the info bars at the top and/or bottom are sticky. The design elements for this page are:

a. the page itself (sizing, spacing of the images, etc.)
b. the interactions (how does a selected heart look, how does that compare to an unselected heart)

ICONS: feel free to come up with your own iconography (ie for the 'chat' icon in the top right, and/or the 'heart' icon signifying you want to meet this person. We really like the fact that the 'matches' and 'calendar' tabs are signified with words rather than icons, but feel free to get creative on this front as well. If you can make it prettier, we're all ears :) Whatever you do on this front, make sure all your icons and the rest of your work are/is free of copyright so we can actually use them in a commercially distributed app.

The winner of this contest may get awarded a follow-up project where they will be asked to design the entire app for us.

Reason: Thank you all for your submissions. We got some promising designs but nothing that was good enough just yet. We gave some feedback for improvement and wanted to give you guys some more time to get it right. New submissions are welcome too of course. Don't hesitate to contact us if you have any questions.

Target Market(s)

singles

Industry/Entity Type

Dating

Requirements
Must have
• fresh, clean, user-friendly design of the 2 pages provided. Your design choices should include decisions about font, sizing, colours, spacing, etc.
Nice to have
• custom icons, see project brief

```html
<!DOCTYPE html>
<html lang="en">
<head>
<meta charset="utf-8">
<title>Vimzy – Matches and Schedule screens</title>
<link rel="stylesheet" href="https://fonts.googleapis.com/css2?family=Roboto:wght@400;500;700&display=swap">
<style>
:root{
  --page-bg:#f6f6f6;
  --status-blue:#0a75a3;
  --bar-blue:#0d8bbd;
  --accent-blue:#1b90c3;
  --screen-bg:#f1f1f1;
  --card-bg:#ffffff;
  --line:#e3e3e3;
  --muted:#b4b4b4;
  --icon-grey:#c9c9c9;
  --white:#ffffff;
}
*{box-sizing:border-box;margin:0;padding:0}
html,body{width:1200px;height:1200px;overflow:hidden}
body{background:var(--page-bg);font-family:"Roboto",Arial,sans-serif;position:relative}

.screen{position:absolute;top:198px;width:456px;height:804px;background:var(--screen-bg);overflow:hidden;box-shadow:0 2px 10px rgba(0,0,0,.08)}
.screen--matches{left:95px}
.screen--schedule{left:649px}

.status-bar{height:29px;background:var(--status-blue);display:flex;justify-content:flex-end;align-items:center;gap:9px;padding-right:8px;color:var(--white);font-size:15px}
.status-bar svg{display:block}

.app-bar{height:61px;background:var(--bar-blue);display:flex;align-items:center;padding:0 20px 0 24px;color:var(--white)}
.app-bar__title{font-size:21px;font-weight:400;margin-left:24px;flex:1;letter-spacing:.2px}

.tabs{height:60px;background:var(--bar-blue);display:flex;position:relative}
.tab{flex:1;display:flex;align-items:center;justify-content:center;font-size:17px;font-weight:500;color:rgba(255,255,255,.65);letter-spacing:.3px;position:relative}
.tab--active{color:var(--white)}
.tab--active::after{content:"";position:absolute;left:0;right:0;bottom:0;height:4px;background:var(--white)}

.sticky-note{position:absolute;left:0;right:0;background:#f8f8f8;color:var(--accent-blue);text-transform:uppercase;text-align:center;font-size:13.5px;font-weight:500;letter-spacing:.6px;line-height:1.3}
.sticky-note--bottom{bottom:0;height:60px;display:flex;flex-direction:column;justify-content:center;border-top:1px solid var(--line)}

/* Matches */
.match-grid{position:absolute;top:150px;left:0;right:0;bottom:60px;display:flex;gap:9px;padding:11px 10px 0 10px;overflow:hidden}
.match-column{flex:1;display:flex;flex-direction:column;gap:14px}
.match-column--right{padding-top:0}
.match-card{background:var(--card-bg);box-shadow:0 1px 2px rgba(0,0,0,.08);flex-shrink:0}
.match-card__photo{position:relative;display:flex;flex-direction:column;justify-content:flex-end;padding:0 12px 10px;color:var(--white)}
.match-card__name{font-size:16px;font-weight:400}
.match-card__role{font-size:11.5px;margin-top:2px;opacity:.95}
.match-card__stats{display:flex;gap:10px;font-size:10.5px;margin-top:3px;align-items:center}
.match-card__stats span{display:flex;align-items:center;gap:3px}
.match-card__actions{height:40px;display:flex;align-items:center}
.match-card__actions > div{flex:1;display:flex;justify-content:center;align-items:center;height:22px}
.match-card__actions > div:first-child{border-right:1px solid var(--line)}

.photo--lara{height:186px;background:linear-gradient(160deg,#8fb86a 0%,#c98a6a 45%,#e0b640 100%)}
.photo--annie{height:221px;background:linear-gradient(170deg,#d8ccbb 0%,#8d6a58 50%,#2f7486 100%)}
.photo--jenna{height:221px;background:linear-gradient(160deg,#6e5a4a 0%,#c08a6c 45%,#a2603f 100%)}
.photo--camille{height:185px;background:linear-gradient(160deg,#6f8a3e 0%,#4c3a2e 50%,#9aa66a 100%)}
.photo--dark{height:90px;background:linear-gradient(170deg,#2b2b2f 0%,#7a8a95 100%)}
.photo--blonde{height:90px;background:linear-gradient(170deg,#c7b49a 0%,#b48a5c 100%)}

/* Schedule */
.sticky-note--top{top:150px;height:62px;display:flex;flex-direction:column;justify-content:center;background:#fbfbfb;border-bottom:1px solid var(--line);z-index:2}
.slot-grid{position:absolute;top:212px;left:14px;right:14px;bottom:60px;overflow:hidden;background:var(--white)}
.slot-row{display:flex;height:57.5px;border-bottom:1px solid var(--line);align-items:center}
.slot{flex:1;height:38px;display:flex;flex-direction:column;align-items:center;justify-content:center;font-size:16px;color:var(--muted);letter-spacing:.5px;border-right:1px solid var(--line)}
.slot:last-child{border-right:none}
.slot--selected{color:var(--accent-blue);font-weight:500}
.slot__day{font-size:11px;letter-spacing:.6px;line-height:1.2}
.slot__time{font-size:11px;letter-spacing:.6px;line-height:1.2}
</style>
</head>
<body>

<section class="screen screen--matches">
  <div class="status-bar">
    <svg width="16" height="13" viewBox="0 0 16 13"><path d="M8 13L0 3a12 12 0 0 1 16 0z" fill="#fff"/></svg>
    <svg width="13" height="13" viewBox="0 0 13 13"><path d="M13 0v13H0z" fill="rgba(255,255,255,.5)"/><path d="M9 4v9H0z" fill="#fff"/></svg>
    <svg width="9" height="15" viewBox="0 0 9 15"><rect x="0" y="2" width="9" height="13" rx="1" fill="#fff"/><rect x="3" y="0" width="3" height="2" fill="#fff"/></svg>
    <span>15:45</span>
  </div>
  <header class="app-bar">
    <svg width="24" height="18" viewBox="0 0 24 18"><rect width="24" height="2.5" fill="#fff"/><rect y="7.7" width="24" height="2.5" fill="#fff"/><rect y="15.5" width="24" height="2.5" fill="#fff"/></svg>
    <h1 class="app-bar__title">Browse Match</h1>
    <svg width="26" height="22" viewBox="0 0 26 22"><path d="M7 0h17a2 2 0 0 1 2 2v10a2 2 0 0 1-2 2h-1v4l-4-4H7a2 2 0 0 1-2-2V2a2 2 0 0 1 2-2z" fill="#fff"/><path d="M3 5v8a3 3 0 0 0 3 3h8l-2 2H6l-4 4v-4H2a2 2 0 0 1-2-2V7a2 2 0 0 1 2-2z" fill="#fff" opacity=".85"/></svg>
  </header>
  <nav class="tabs">
    <div class="tab tab--active">MATCHES</div>
    <div class="tab">SCHEDULE</div>
  </nav>

  <div class="match-grid">
    <div class="match-column">
      <article class="match-card">
        <div class="match-card__photo photo--lara" role="img" aria-label="Profile photo of Lara">
          <div class="match-card__name">Lara, 24</div>
          <div class="match-card__role">Architect at KVA</div>
          <div class="match-card__stats"><span>&#9673; 5</span><span>&#9679;&#9679; 12</span></div>
        </div>
        <div class="match-card__actions">
          <div><svg width="16" height="14" viewBox="0 0 16 14"><path d="M8 14L1.2 7.2A4 4 0 0 1 8 1.6a4 4 0 0 1 6.8 5.6z" fill="var(--accent-blue)"/></svg></div>
          <div><svg width="12" height="12" viewBox="0 0 12 12"><path d="M1 1l10 10M11 1L1 11" stroke="var(--icon-grey)" stroke-width="1.6"/></svg></div>
        </div>
      </article>
      <article class="match-card">
        <div class="match-card__photo photo--jenna" role="img" aria-label="Profile photo of Jenna">
          <div class="match-card__name">Jenna, 31</div>
          <div class="match-card__role">Comunity Manager</div>
          <div class="match-card__stats"><span>&#9673; 9</span><span>&#9679;&#9679; 3</span></div>
        </div>
        <div class="match-card__actions">
          <div><svg width="16" height="14" viewBox="0 0 16 14"><path d="M8 14L1.2 7.2A4 4 0 0 1 8 1.6a4 4 0 0 1 6.8 5.6z" fill="var(--icon-grey)"/></svg></div>
          <div><svg width="12" height="12" viewBox="0 0 12 12"><path d="M1 1l10 10M11 1L1 11" stroke="var(--icon-grey)" stroke-width="1.6"/></svg></div>
        </div>
      </article>
      <article class="match-card">
        <div class="match-card__photo photo--dark" role="img" aria-label="Profile photo of another match"></div>
      </article>
    </div>
    <div class="match-column match-column--right">
      <article class="match-card">
        <div class="match-card__photo photo--annie" role="img" aria-label="Profile photo of Annie">
          <div class="match-card__name">Annie, 21</div>
          <div class="match-card__role">Law Student</div>
          <div class="match-card__stats"><span>&#9673; 6</span><span>&#9679;&#9679; 4</span></div>
        </div>
        <div class="match-card__actions">
          <div><svg width="16" height="14" viewBox="0 0 16 14"><path d="M8 14L1.2 7.2A4 4 0 0 1 8 1.6a4 4 0 0 1 6.8 5.6z" fill="var(--icon-grey)"/></svg></div>
          <div><svg width="12" height="12" viewBox="0 0 12 12"><path d="M1 1l10 10M11 1L1 11" stroke="var(--icon-grey)" stroke-width="1.6"/></svg></div>
        </div>
      </article>
      <article class="match-card">
        <div class="match-card__photo photo--camille" role="img" aria-label="Profile photo of Camille">
          <div class="match-card__name">Camille, 25</div>
          <div class="match-card__role">Journalism Student</div>
          <div class="match-card__stats"><span>&#9673; 8</span><span>&#9679;&#9679; 12</span></div>
        </div>
        <div class="match-card__actions">
          <div><svg width="16" height="14" viewBox="0 0 16 14"><path d="M8 14L1.2 7.2A4 4 0 0 1 8 1.6a4 4 0 0 1 6.8 5.6z" fill="var(--icon-grey)"/></svg></div>
          <div><svg width="12" height="12" viewBox="0 0 12 12"><path d="M1 1l10 10M11 1L1 11" stroke="var(--icon-grey)" stroke-width="1.6"/></svg></div>
        </div>
      </article>
      <article class="match-card">
        <div class="match-card__photo photo--blonde" role="img" aria-label="Profile photo of another match"></div>
      </article>
    </div>
  </div>

  <footer class="sticky-note sticky-note--bottom">
    <div>Excellent! You can <svg width="13" height="11" viewBox="0 0 16 14"><path d="M8 14L1.2 7.2A4 4 0 0 1 8 1.6a4 4 0 0 1 6.8 5.6z" fill="var(--accent-blue)"/></svg> more if you'd like</div>
    <div>Next, share your schedule with us!</div>
  </footer>
</section>

<section class="screen screen--schedule">
  <div class="status-bar">
    <svg width="16" height="13" viewBox="0 0 16 13"><path d="M8 13L0 3a12 12 0 0 1 16 0z" fill="#fff"/></svg>
    <svg width="13" height="13" viewBox="0 0 13 13"><path d="M13 0v13H0z" fill="rgba(255,255,255,.5)"/><path d="M9 4v9H0z" fill="#fff"/></svg>
    <svg width="9" height="15" viewBox="0 0 9 15"><rect x="0" y="2" width="9" height="13" rx="1" fill="#fff"/><rect x="3" y="0" width="3" height="2" fill="#fff"/></svg>
    <span>15:45</span>
  </div>
  <header class="app-bar">
    <svg width="24" height="18" viewBox="0 0 24 18"><rect width="24" height="2.5" fill="#fff"/><rect y="7.7" width="24" height="2.5" fill="#fff"/><rect y="15.5" width="24" height="2.5" fill="#fff"/></svg>
    <h1 class="app-bar__title">Schedule</h1>
    <svg width="26" height="22" viewBox="0 0 26 22"><path d="M7 0h17a2 2 0 0 1 2 2v10a2 2 0 0 1-2 2h-1v4l-4-4H7a2 2 0 0 1-2-2V2a2 2 0 0 1 2-2z" fill="#fff"/><path d="M3 5v8a3 3 0 0 0 3 3h8l-2 2H6l-4 4v-4H2a2 2 0 0 1-2-2V7a2 2 0 0 1 2-2z" fill="#fff" opacity=".85"/></svg>
  </header>
  <nav class="tabs">
    <div class="tab">MATCHES</div>
    <div class="tab tab--active">SCHEDULE</div>
  </nav>

  <div class="sticky-note sticky-note--top">
    <div>Choose when you're available.</div>
    <div>We'll schedule your dates for you!</div>
  </div>

  <div class="slot-grid">
    <div class="slot-row">
      <div class="slot"><span class="slot__day">TODAY</span><span class="slot__time">13:00</span></div>
      <div class="slot">14:00</div><div class="slot">15:00</div><div class="slot">16:00</div>
    </div>
    <div class="slot-row">
      <div class="slot">17:00</div><div class="slot">18:00</div>
      <div class="slot slot--selected">19:00</div><div class="slot slot--selected">20:00</div>
    </div>
    <div class="slot-row">
      <div class="slot slot--selected">21:00</div><div class="slot slot--selected">22:00</div><div class="slot slot--selected">23:00</div>
      <div class="slot slot--selected"><span class="slot__day">TOMORROW</span><span class="slot__time">00:00</span></div>
    </div>
    <div class="slot-row">
      <div class="slot slot--selected">01:00</div><div class="slot slot--selected">02:00</div>
      <div class="slot slot--selected">03:00</div><div class="slot slot--selected">04:00</div>
    </div>
    <div class="slot-row">
      <div class="slot slot--selected">05:00</div><div class="slot slot--selected">06:00</div>
      <div class="slot">07:00</div><div class="slot">08:00</div>
    </div>
    <div class="slot-row">
      <div class="slot">09:00</div><div class="slot">10:00</div><div class="slot">11:00</div><div class="slot">12:00</div>
    </div>
    <div class="slot-row">
      <div class="slot">13:00</div><div class="slot">14:00</div><div class="slot">15:00</div><div class="slot">16:00</div>
    </div>
    <div class="slot-row">
      <div class="slot">17:00</div><div class="slot">18:00</div>
      <div class="slot slot--selected">19:00</div><div class="slot slot--selected">20:00</div>
    </div>
    <div class="slot-row">
      <div class="slot slot--selected">21:00</div><div class="slot slot--selected">22:00</div><div class="slot slot--selected">23:00</div>
      <div class="slot"><span class="slot__day">FRIDAY</span><span class="slot__time">00:00</span></div>
    </div>
    <div class="slot-row">
      <div class="slot">01:00</div><div class="slot">02:00</div><div class="slot">03:00</div><div class="slot">04:00</div>
    </div>
  </div>

  <footer class="sticky-note sticky-note--bottom">
    <div>Select the one hour blocks in which you're</div>
    <div>available to meet up with your matches.</div>
  </footer>
</section>

</body>
</html>
```